Adorable Luxury Flower Shop

Need a beautiful, eye catching, elegant full-service website.
INSPIRATIONS ARE;
https://www.quillmoreblooms.com

Industry/Entity Type

retail, floral, boutique

Coding

Coded - Design and coding required

Number of Pages Required

3 page

Requirements
Must have
• SEO, Coded, UX, Fully responsive mobile, tablet, desktop, Ecommerce setup with Square, payments integration (if we use squarespace). SEO optimization with keywords, tags, meta descriptions, Load speed optimization, plain circle my business setup.
Nice to have
• pictures, color, elegance

```html
<!DOCTYPE html>
<html lang="en">
<head>
<meta charset="utf-8">
<title>Quillmore Flower Boutique</title>
<link href="https://fonts.googleapis.com/css2?family=Urbanist:wght@400;500;600;700&display=swap" rel="stylesheet">
<style>
:root{
  --red:#c8161d;
  --ink:#111111;
  --body:#4a4a4a;
  --blush:#fcf0f0;
  --soft:#f7f4f4;
  --footer:#2b2b2b;
  --white:#ffffff;
}
*{margin:0;padding:0;box-sizing:border-box}
html,body{width:1200px;height:4189px;overflow:hidden;background:var(--white)}
body{position:relative;font-family:"Urbanist",sans-serif;color:var(--ink)}
.abs{position:absolute}
.photo{position:absolute}
/* header */
.nav-link{position:absolute;top:30px;font-size:14px;font-weight:500;text-transform:uppercase;color:var(--ink)}
.nav-link.active{color:var(--red)}
.corner-bloom{left:0;top:0;width:140px;height:60px;background:radial-gradient(ellipse at 30% 30%,#f4c3cf,#fde9ee 60%,transparent 75%)}
.logo-bump{left:485px;top:0;width:230px;height:135px;background:var(--white);border-radius:0 0 115px 115px;z-index:2}
.brand{position:absolute;left:0;right:0;text-align:center;font-weight:700;font-size:30px;letter-spacing:1px;text-transform:uppercase}
.icon-btn{position:absolute;top:24px;width:30px;height:30px;border:1.5px solid var(--red);border-radius:50%;display:flex;align-items:center;justify-content:center}
/* hero */
.hero{left:70px;top:76px;width:1060px;height:493px;border-radius:10px;overflow:hidden;background:linear-gradient(180deg,#eef3f3 0%,#dfe9ea 45%,#f0c3c8 75%,#d9868f 100%)}
.hero h1{position:absolute;left:0;right:0;top:96px;text-align:center;font-size:32px;font-weight:600;line-height:50px;text-transform:uppercase}
.hero h1 span{color:var(--red)}
.section-title{position:absolute;left:0;right:0;text-align:center;font-size:32px;font-weight:600;text-transform:uppercase}
/* best sellers */
.cat{position:absolute;top:741px;width:315px;height:239px;border-radius:10px;overflow:hidden}
.cat .art{position:absolute;right:10px;top:20px;width:150px;height:200px;border-radius:50% 50% 8px 8px}
.cat .name{position:absolute;left:27px;font-size:17px;font-weight:600;line-height:28px;color:var(--red);text-transform:uppercase}
.cat .shop{position:absolute;left:27px;top:200px;font-size:12px;font-weight:600;text-transform:uppercase}
/* about */
.about-photo{left:0;top:1068px;width:600px;height:514px;background:linear-gradient(135deg,#8a7a60,#4f6a4a 40%,#c66373 70%,#8b8070)}
.about-panel{left:600px;top:1068px;width:600px;height:514px;background:var(--soft)}
.side-title{position:absolute;font-size:32px;font-weight:600;text-transform:uppercase;line-height:56px}
.copy{position:absolute;font-size:15px;line-height:34px;color:var(--body)}
.btn{position:absolute;height:46px;border-radius:23px;background:var(--red);color:var(--white);font-size:16px;font-weight:600;text-transform:uppercase;display:flex;align-items:center;justify-content:center}
/* products */
.prod{position:absolute;top:1756px;width:232px;height:364px;border-radius:10px;background:var(--blush)}
.prod .art{position:absolute;left:36px;top:20px;width:160px;height:190px;border-radius:50% 50% 10px 10px}
.prod .name{position:absolute;left:21px;top:234px;font-size:16px;font-weight:500;line-height:31px;color:var(--red);text-transform:uppercase}
.prod .price{position:absolute;left:21px;top:312px;font-size:17px;font-weight:600}
.prod .cart{position:absolute;right:15px;top:306px;width:40px;height:40px;border:1.5px solid var(--red);border-radius:5px;display:flex;align-items:center;justify-content:center}
/* discount */
.promo{left:0;top:2297px;width:1200px;height:438px;background:radial-gradient(ellipse at 8% 50%,#f6b8bd 0%,transparent 35%),radial-gradient(ellipse at 95% 60%,#f6b8bd 0%,transparent 30%),#fdf8f6}
/* reviews */
.review{position:absolute;top:2821px;width:262px;height:330px;border:1.5px solid #eeeeee;border-radius:8px;background:var(--white);text-align:center}
.review .stars{margin-top:30px;color:#f5c02a;font-size:18px;letter-spacing:4px}
.review .when{margin-top:12px;font-size:13px;color:var(--red);text-transform:uppercase}
.review p{margin:14px 18px 0;font-size:13px;line-height:34px;color:var(--body)}
.review .who{position:absolute;left:52px;top:262px;display:flex;align-items:center;gap:20px;text-align:left}
.avatar{width:40px;height:40px;border-radius:50%;background:var(--red);color:var(--white);font-weight:600;font-size:16px;display:flex;align-items:center;justify-content:center}
.who b{display:block;font-size:13px;font-weight:500;color:var(--red);text-transform:uppercase}
.who small{display:block;margin-top:10px;font-size:13px;color:var(--body)}
/* store */
.store-photo{left:600px;top:3239px;width:600px;height:512px;background:linear-gradient(140deg,#4a5a34,#c7a47a 35%,#e7a6bf 55%,#a88ad0 70%,#d9b994)}
/* footer */
.footer{left:0;top:3840px;width:1200px;height:349px;background:var(--footer);color:var(--white)}
.foot-nav{position:absolute;top:222px;left:0;right:0;display:flex;justify-content:center;gap:56px;font-size:15px;font-weight:500;text-transform:uppercase}
.copyright{position:absolute;top:276px;left:0;right:0;text-align:center;font-size:14px;font-weight:500;text-transform:uppercase}
</style>
</head>
<body>

<header>
  <div class="photo abs corner-bloom" role="img" aria-label="Pink lily blossoms in the top corner"></div>
  <a class="nav-link active" style="left:172px">Home</a>
  <a class="nav-link" style="left:264px">About Us</a>
  <a class="nav-link" style="left:387px">Shop</a>
  <a class="nav-link" style="left:767px">Blog</a>
  <a class="nav-link" style="left:856px">Contact</a>
  <span class="icon-btn" style="left:974px"><svg width="12" height="12" viewBox="0 0 12 12"><circle cx="5" cy="5" r="3.5" fill="none" stroke="#111" stroke-width="1.5"/><line x1="7.6" y1="7.6" x2="11" y2="11" stroke="#111" stroke-width="1.5"/></svg></span>
  <span class="icon-btn" style="left:1025px"><svg width="14" height="14" viewBox="0 0 14 14" fill="none" stroke="#111" stroke-width="1.3"><path d="M1 2h2l2 7h6l1.5-5H4"/><circle cx="6" cy="12" r="1"/><circle cx="10" cy="12" r="1"/></svg></span>
  <div class="abs logo-bump"><span class="brand" style="top:58px;color:var(--ink)">Quillmore</span></div>
</header>

<section class="hero abs" role="img" aria-label="Pink cosmos flowers against a pale sky">
  <h1>When you think of <span>flowers</span><br>think of ours.</h1>
</section>

<h2 class="section-title" style="top:645px">Best Sellers</h2>
<div class="cat" style="left:111px;background:linear-gradient(135deg,#fde6df,#fdf1e8)">
  <div class="art" role="img" aria-label="Bouquet of white and pink roses" style="background:linear-gradient(#f1d6d6,#e7c7bd)"></div>
  <div class="name" style="top:123px">Wedding<br>Flowers</div>
  <div class="shop">Shop now &rarr;</div>
</div>
<div class="cat" style="left:444px;background:linear-gradient(135deg,#fbf4d9,#eef5e6 50%,#e7eefa)">
  <div class="art" role="img" aria-label="White magnolias in a glass vase" style="background:linear-gradient(#f2eee6,#d8dbd6)"></div>
  <div class="name" style="top:151px">Subscriptions</div>
  <div class="shop">Shop now &rarr;</div>
</div>
<div class="cat" style="left:774px;background:linear-gradient(135deg,#fde4ec,#f4e6fb)">
  <div class="art" role="img" aria-label="Bouquet of sunflowers and lavender" style="background:linear-gradient(#e9c24a,#8f8ab8 60%,#6d8a4b)"></div>
  <div class="name" style="top:123px">Seasonal<br>Bouquets</div>
  <div class="shop">Shop now &rarr;</div>
</div>

<div class="photo about-photo" role="img" aria-label="Florist arranging bouquets in a flower warehouse"></div>
<section class="abs about-panel">
  <h2 class="side-title" style="left:65px;top:45px">About Quillmore</h2>
  <p class="copy" style="left:65px;top:121px;width:430px">Lorem ipsum dolor sit amet, consectetur adipiscing elit, sed do eiusmod tempor incididunt ut labore et dolore magna aliqua.</p>
  <p class="copy" style="left:65px;top:241px;width:430px">Lorem ipsum dolor sit amet, consectetur adipiscing elit, sed do eiusmod tempor incididunt ut labore et dolore magna sint occaecat cupidatat non proident, sunt in culpa qui officia deserunt mollit anim id est laborum.</p>
  <a class="btn" style="left:65px;top:416px;width:143px">Shop now</a>
</section>

<h2 class="section-title" style="top:1656px">Our Products &amp; Arrivals</h2>
<div class="prod" style="left:111px"><div class="art" role="img" aria-label="Pink and white rose bouquet" style="background:linear-gradient(#f3d2d6,#dfe6d6)"></div><div class="name">Timeless Rose<br>Bouquet</div><div class="price">$50 - $150</div><span class="cart"><svg width="18" height="18" viewBox="0 0 14 14" fill="none" stroke="#111" stroke-width="1.1"><path d="M1 2h2l2 7h6l1.5-5H4"/><circle cx="6" cy="12" r="1"/><circle cx="10" cy="12" r="1"/></svg></span></div>
<div class="prod" style="left:359px"><div class="art" role="img" aria-label="Bright mixed bouquet with orchids" style="background:linear-gradient(#f07aa8,#f4d34c 60%,#7aa35a)"></div><div class="name">Vibrant Orchid<br>Bouquet</div><div class="price">$75 - $150</div><span class="cart"><svg width="18" height="18" viewBox="0 0 14 14" fill="none" stroke="#111" stroke-width="1.1"><path d="M1 2h2l2 7h6l1.5-5H4"/><circle cx="6" cy="12" r="1"/><circle cx="10" cy="12" r="1"/></svg></span></div>
<div class="prod" style="left:608px"><div class="art" role="img" aria-label="Spring blossom bouquet in red and pink" style="background:linear-gradient(#e2566a,#f3b6c4 60%,#6d9a55)"></div><div class="name">Spring Blossom<br>Bouquet</div><div class="price">$45 - $100</div><span class="cart"><svg width="18" height="18" viewBox="0 0 14 14" fill="none" stroke="#111" stroke-width="1.1"><path d="M1 2h2l2 7h6l1.5-5H4"/><circle cx="6" cy="12" r="1"/><circle cx="10" cy="12" r="1"/></svg></span></div>
<div class="prod" style="left:857px"><div class="art" role="img" aria-label="Red rose bouquet" style="background:linear-gradient(#c81a24,#8e1118 60%,#4f6a3a)"></div><div class="name">Luxury Lily and Rose<br>Bouquet</div><div class="price">$85 - $200</div><span class="cart"><svg width="18" height="18" viewBox="0 0 14 14" fill="none" stroke="#111" stroke-width="1.1"><path d="M1 2h2l2 7h6l1.5-5H4"/><circle cx="6" cy="12" r="1"/><circle cx="10" cy="12" r="1"/></svg></span></div>
<a class="btn" style="left:481px;top:2172px;width:238px">View more products</a>

<section class="abs promo" role="img" aria-label="Soft watercolor pink flowers framing the offer">
  <h2 class="section-title" style="top:76px">Discounted Floral Bliss</h2>
  <p class="abs" style="left:0;right:0;top:150px;text-align:center;font-size:25px;font-weight:600;color:var(--red);text-transform:uppercase">Save big with 30% off</p>
  <p class="copy" style="left:300px;top:210px;width:600px;text-align:center;font-size:17px;line-height:39px">Lorem ipsum dolor sit amet, consectetur adipiscing elit, sed do eiusmod tempor incididunt ut labore et dolore magna.</p>
  <a class="btn" style="left:528px;top:318px;width:144px">Shop now</a>
</section>

<section>
  <h2 class="side-title" style="left:110px;top:2803px">Client's<br>Reviews</h2>
  <div class="abs" style="left:110px;top:2935px;color:#f5c02a;font-size:24px;letter-spacing:5px">★★★★★</div>
  <div class="abs" style="left:110px;top:2988px;display:flex;align-items:center;gap:16px;font-size:15px;font-weight:500;text-transform:uppercase"><span style="width:16px;height:16px;border-radius:50%;background:#4a86e8;display:inline-block"></span>5 Reviews</div>
  <div class="review" style="left:407px"><div class="stars">★★★★★</div><div class="when">4 months ago</div><p>Lorem ipsum dolor sit amet, consectetur adipiscing elit, sed do eiusmod tempor incididunt ut labore et dolore magna.</p><div class="who"><span class="avatar">H</span><div><b>Hazel Dunmore</b><small>10/3/2024</small></div></div></div>
  <div class="review" style="left:696px"><div class="stars">★★★★★</div><div class="when">A year ago</div><p>Lorem ipsum dolor sit amet, consectetur adipiscing elit, sed do eiusmod tempor incididunt ut labore et dolore magna.</p><div class="who"><span class="avatar">N</span><div><b>Nora Reyes</b><small>9/11/2023</small></div></div></div>
  <div class="review" style="left:985px"><div class="stars">★★★★★</div><div class="when">A year ago</div><p>Lorem ipsum dolor sit amet, consectetur adipiscing elit, sed do eiusmod tempor incididunt ut labore et dolore magna.</p><div class="who"><span class="avatar">H</span><div><b>Harriet Moyle</b><small>5/3/2023</small></div></div></div>
</section>

<section>
  <h2 class="side-title" style="left:110px;top:3255px">Find Meadowlark at<br>Greenvale Market</h2>
  <p class="copy" style="left:112px;top:3389px;width:420px">Lorem ipsum dolor sit amet, consectetur adipiscing elit, sed do eiusmod tempor incididunt ut labore et dolore magna aliqua.</p>
  <p class="copy" style="left:112px;top:3509px;width:420px">Lorem ipsum dolor sit amet, consectetur adipiscing elit, sed do eiusmod tempor incididunt ut labore et dolore magna sint occaecat cupidatat non proident, sunt in culpa qui officia deserunt mollit anim id est laborum.</p>
  <a class="btn" style="left:112px;top:3684px;width:205px">Find your store!</a>
  <div class="photo store-photo" role="img" aria-label="Colorful mixed bouquet wrapped in kraft paper"></div>
</section>

<footer class="abs footer">
  <span class="brand" style="top:95px;color:var(--white);font-size:34px">Quillmore</span>
  <nav class="foot-nav"><a>Home</a><a>About Us</a><a>Shop</a><a>Blog</a><a>Reviews</a><a>Contact</a></nav>
  <p class="copyright">©2025 Copyrights &nbsp;|&nbsp; All rights reserved</p>
</footer>

</body>
</html>
```